Window cleaning company in need of leaflet design

Family run business requires leaflet design.
Our company uses water fed pole with pure water which is what the leaflet needs to emphasise on (include a background picture of a water fed pole cleaning a window.)

other services we offer which i would like to include are:
• facia/soffit cleaning.
• Conservatory cleans.
• Gutter clearing which is performed by a gutter vacuum pictures of gutters before and after clean are provided to every customer if they require.
• pressure washing

uploaded company logo to be included on leaflet.
number to include is 07715264389
email address is Rtglasscare@mailbay.test
would also like a facebook symbol included to show we are on social media.
Thank you

Font styles to use
Serif
Sans Serif

Colors
00a990
33a6d7
3276b5
3277b5
34a7d8
87cfc6
33b8a4
cfdfed
85acd3

Requirements
Must have
• We use traditional and water fed pole methods of cleaning. So those hard to reach or awkward to clean windows are not a problem. No need for ladders.

Our water fed pole system uses 100% pure water. This is water that has been de-ironised and de-mineralised to ensue it’s perfectly pure for a spot free finish.

• fully insured

• regular and reliable service
• one off cleans available

Call dean on 07715264389 for a free quote

```html
<!DOCTYPE html>
<html lang="en">
<head>
<meta charset="utf-8">
<title>R.T Window Cleaning – Leaflet</title>
<link href="https://fonts.googleapis.com/css2?family=Roboto:wght@400;500;700;900&family=Roboto+Condensed:wght@400;700&display=swap" rel="stylesheet">
<style>
  :root{
    --teal:#00a990;
    --teal-soft:#33b8a4;
    --sky:#1ea3e0;
    --blue:#1466c2;
    --navy:#1f3592;
    --ink:#222831;
    --paper:#f6f8f9;
    --white:#ffffff;
  }
  *{margin:0;padding:0;box-sizing:border-box}
  html,body{width:960px;height:1200px;overflow:hidden;background:var(--paper)}
  .leaflet{position:relative;width:960px;height:1200px;overflow:hidden;background:var(--paper);font-family:"Roboto",sans-serif;color:var(--ink)}
  .artwork{position:absolute;inset:0}
  .brand-name{position:absolute;left:88px;top:530px;font-family:"Roboto Condensed",sans-serif;font-weight:400;font-size:52px;color:var(--navy);letter-spacing:.3px;white-space:nowrap}
  .services-title{position:absolute;left:90px;top:604px;width:445px;height:71px;background:var(--teal);color:var(--white);font-weight:900;font-size:43px;line-height:71px;padding-left:37px;letter-spacing:.5px}
  .services-list{position:absolute;left:100px;top:693px;list-style:none}
  .services-list li{display:flex;align-items:center;height:38px;font-family:"Roboto Condensed",sans-serif;font-weight:700;font-size:22px;color:var(--ink);letter-spacing:.3px}
  .services-list svg{width:24px;height:24px;margin-right:12px;flex:none}
  .gutter-shot{position:absolute;top:699px;width:178px;height:139px;border:4px solid var(--teal-soft);overflow:hidden}
  .gutter-shot.before{left:487px;background:linear-gradient(160deg,#5c5f63 0%,#7d7a74 45%,#9b8a72 70%,#7a4a38 100%)}
  .gutter-shot.after{left:704px;background:linear-gradient(160deg,#5d6166 0%,#8b8e91 45%,#e9ecee 62%,#8c4a36 100%)}
  .ribbon{position:absolute;top:687px;width:70px;height:70px;overflow:hidden}
  .ribbon span{position:absolute;left:-24px;top:20px;width:110px;transform:rotate(-45deg);background:var(--blue);color:var(--white);font-size:11px;font-weight:500;text-align:center;line-height:17px;letter-spacing:.5px}
  .ribbon.before{left:483px}
  .ribbon.after{left:700px}
  .about{position:absolute;left:90px;width:830px;padding-left:22px;border-left:2px solid var(--teal);font-size:17.3px;line-height:22.5px;color:var(--ink)}
  .about.first{top:872px}
  .about.second{top:937px}
  .promises{position:absolute;left:68px;top:1007px;width:830px;height:24px}
  .promise{position:absolute;top:0;display:flex;align-items:center;white-space:nowrap;font-family:"Roboto Condensed",sans-serif;font-weight:700;font-size:19px;color:var(--blue)}
  .promise svg{width:19px;height:19px;margin-right:7px}
  .footer-band{position:absolute;left:0;top:1097px;width:960px;height:103px;background:var(--teal)}
  .quote-bar{position:absolute;left:50px;top:1046px;width:859px;height:90px;border-radius:45px;background:var(--blue);border:2px solid var(--white)}
  .quote-lead{position:absolute;left:50px;top:1046px;width:350px;height:90px;border-radius:45px;background:var(--sky);border:2px solid var(--white)}
  .quote-lead .line-one{position:absolute;left:42px;top:10px;font-size:26px;font-weight:400;color:var(--white);letter-spacing:.3px;white-space:nowrap}
  .quote-lead .line-one b{font-weight:700}
  .quote-lead .line-two{position:absolute;left:42px;top:36px;font-size:41px;font-weight:900;color:var(--white);white-space:nowrap;line-height:46px}
  .phone-badge{position:absolute;left:364px;top:1056px;width:66px;height:66px;border-radius:50%;background:var(--teal-soft);border:4px solid var(--white);display:flex;align-items:center;justify-content:center}
  .phone-badge svg{width:40px;height:40px}
  .phone-number{position:absolute;left:446px;top:1044px;font-weight:900;font-size:68px;line-height:92px;color:var(--white);letter-spacing:.5px;white-space:nowrap}
  .contact-line{position:absolute;left:97px;top:1148px;display:flex;align-items:center;font-size:20px;color:var(--white);white-space:nowrap}
  .contact-line .email-icon{width:20px;height:15px;margin:0 8px 0 20px}
  .contact-line .email{font-weight:700;font-size:20.5px}
  .contact-line .divider{margin:0 28px;font-weight:300}
  .contact-line .social{font-weight:700}
  .contact-line .social-dot{width:22px;height:22px;border-radius:50%;background:#4a5ca8;margin-left:12px}
</style>
</head>
<body>
<main class="leaflet">
  <svg class="artwork" width="960" height="1200" viewBox="0 0 960 1200">
    <defs>
      <linearGradient id="poleShotTone" x1="0" y1="0" x2="1" y2="1">
        <stop offset="0" stop-color="#c9c2b3"/>
        <stop offset=".35" stop-color="#8a6f5d"/>
        <stop offset=".6" stop-color="#6d7f93"/>
        <stop offset="1" stop-color="#b9c9d8"/>
      </linearGradient>
      <linearGradient id="cleanerShotTone" x1="0" y1="0" x2="1" y2="1">
        <stop offset="0" stop-color="#5e8f4c"/>
        <stop offset=".4" stop-color="#9fb0c8"/>
        <stop offset=".75" stop-color="#2f4fa8"/>
        <stop offset="1" stop-color="#d8d6c8"/>
      </linearGradient>
    </defs>
    <path d="M396 0 H960 V498 L800 640 Q769 668 738 640 L300 292 Z" fill="url(#poleShotTone)" role="img" aria-label="Photo of a water fed pole brush spraying pure water onto a window"/>
    <path d="M853 622 Q890 628 918 600 L960 555 V470 L900 525 Q870 560 853 622 Z" fill="var(--teal-soft)"/>
    <path d="M0 0 H430 L488 96 Q505 123 485 145 L190 440 Q162 468 130 444 L0 343 Z" fill="url(#cleanerShotTone)" role="img" aria-label="Photo of a window cleaner wiping glass with a cloth and spray bottle"/>
    <path d="M263 388 Q300 398 335 372 L392 318 L368 300 Z" fill="var(--sky)"/>
  </svg>

  <h1 class="brand-name">R.T Window Cleaning</h1>

  <h2 class="services-title">OUR SERVICES</h2>
  <ul class="services-list">
    <li><svg viewBox="0 0 24 24"><circle cx="12" cy="12" r="10.5" fill="none" stroke="#1466c2" stroke-width="1.8"/><path d="M7 12.3l3.4 3.3L17 9" fill="none" stroke="#1466c2" stroke-width="1.8"/></svg>FACIA/SOFFIT CLEANING</li>
    <li><svg viewBox="0 0 24 24"><circle cx="12" cy="12" r="10.5" fill="none" stroke="#1466c2" stroke-width="1.8"/><path d="M7 12.3l3.4 3.3L17 9" fill="none" stroke="#1466c2" stroke-width="1.8"/></svg>CONSERVATORY CLEANS</li>
    <li><svg viewBox="0 0 24 24"><circle cx="12" cy="12" r="10.5" fill="none" stroke="#1466c2" stroke-width="1.8"/><path d="M7 12.3l3.4 3.3L17 9" fill="none" stroke="#1466c2" stroke-width="1.8"/></svg>GUTTER CLEARING</li>
    <li><svg viewBox="0 0 24 24"><circle cx="12" cy="12" r="10.5" fill="none" stroke="#1466c2" stroke-width="1.8"/><path d="M7 12.3l3.4 3.3L17 9" fill="none" stroke="#1466c2" stroke-width="1.8"/></svg>PRESSURE WASHING</li>
  </ul>

  <div class="gutter-shot before" role="img" aria-label="Photo of a roof gutter full of leaves before clearing"></div>
  <div class="gutter-shot after" role="img" aria-label="Photo of the same roof gutter clean after clearing"></div>
  <div class="ribbon before"><span>BEFORE</span></div>
  <div class="ribbon after"><span>AFTER</span></div>

  <p class="about first">We use traditional and water fed pole methods of cleaning. So those hard to reach or awkward to clean windows are not a problem. No need for ladders.</p>
  <p class="about second">Our water fed pole system uses 100% pure water. This is water that has been de-ironised and de-mineralised to ensue it’s perfectly pure for a spot free finish.</p>

  <div class="promises">
    <span class="promise" style="left:0"><svg viewBox="0 0 24 24"><circle cx="12" cy="12" r="10.5" fill="none" stroke="#00a990" stroke-width="1.8"/><path d="M7 12.3l3.4 3.3L17 9" fill="none" stroke="#00a990" stroke-width="1.8"/></svg>FULLY INSURED</span>
    <span class="promise" style="left:195px"><svg viewBox="0 0 24 24"><circle cx="12" cy="12" r="10.5" fill="none" stroke="#00a990" stroke-width="1.8"/><path d="M7 12.3l3.4 3.3L17 9" fill="none" stroke="#00a990" stroke-width="1.8"/></svg>REGULAR AND RELIABLE SERVICE</span>
    <span class="promise" style="left:545px"><svg viewBox="0 0 24 24"><circle cx="12" cy="12" r="10.5" fill="none" stroke="#00a990" stroke-width="1.8"/><path d="M7 12.3l3.4 3.3L17 9" fill="none" stroke="#00a990" stroke-width="1.8"/></svg>ONE OFF CLEANS AVAILABLE</span>
  </div>

  <div class="footer-band"></div>
  <div class="quote-bar"></div>
  <div class="quote-lead">
    <span class="line-one">CALL <b>DEAN</b> FOR A</span>
    <span class="line-two">FREE QUOTE</span>
  </div>
  <div class="phone-badge">
    <svg viewBox="0 0 24 24"><path d="M6.6 3.5l2.6 3.1c.4.5.4 1.2-.1 1.7L7.7 9.6c.9 2.4 3.2 4.9 5.7 6l1.4-1.4c.5-.5 1.2-.5 1.7-.1l3 2.5c.5.4.6 1.2.1 1.7l-1.7 1.9c-.6.6-1.5.8-2.3.5C9.7 18.4 5.5 14 3.4 8.3c-.3-.8 0-1.7.6-2.2l1.6-2.6c.3-.4.7-.4 1 0z" fill="#ffffff"/></svg>
  </div>
  <div class="phone-number">07715264389</div>

  <div class="contact-line">
    <span>For more info mail us:</span>
    <svg class="email-icon" viewBox="0 0 20 15"><rect x="1" y="1" width="18" height="13" fill="none" stroke="#fff" stroke-width="1.4"/><path d="M1 1l9 7 9-7" fill="none" stroke="#fff" stroke-width="1.4"/></svg>
    <span class="email">Rtglasscare@mailbay.test</span>
    <span class="divider">|</span>
    <span class="social">Find us on</span>
    <span class="social-dot"></span>
  </div>
</main>
</body>
</html>
```